Loft Merchandise Email Marketing Template

ATTN DESIGNERS, UPDATED BRIEF! 3 JAN 2015.

- Email marketing template to promote our items.
- 7 items per email
- 1 main featured item on the top section - MUST BE ABOVE THE FOLD.
- every items with "call to action" buttonS (REQUEST SAMPLE button in grey colour and BUY NOW button in green colour).
- Red theme, but not too much.
- smart, simple AND MODERN feel
- our company logo attached.
- go to www.loftmerchandise.example.au to understand our company.
- FOLLOW THIS DESIGN / FEEL.
http://view.e.brightvisor.example.au/?j=abcd123456789012&m=ab1234567890123456&ls=ab1234567890123456789012&l=ab1234567890&s=ab123456789012345678&jb=ab12345678&ju=ab123456789012345678&r=0
- design submitted to be in EPS form, all layers neatly grouped and labelled.

Project Deadline Extended
Reason: Designs submitted are not satisfactory. We are still open for your submissions. Smart, simple, fun, creative feel desired. Red and grey colour theme. 7 items per email with 1 main featured item (larger display) at the top. Each items to have a "call to action" button. i.e. "REQUEST SAMPLE" button.

Target Market(s)

the target markets are marketing managers that are in charge of their companies marketing campaign, and the buying of promotional merchandises.

these guys ( the marketing manager, my target market) are busy, constantly under the pump, and results oriented.

Industry/Entity Type

Marketing

Font styles to use
Sans Serif

Colors
eb1f27

Requirements
Must have
• SMART, SMART AND SMART.
SIMPLE, CLEAN LOOK.
Should not have
• DULL, slow, wimpy look.

```html
<!DOCTYPE html>
<html lang="en">
<head>
<meta charset="utf-8">
<title>Loft Merchandise Newsletter</title>
<link href="https://fonts.googleapis.com/css2?family=Arimo:wght@400;700&display=swap" rel="stylesheet">
<style>
  :root {
    --red: #eb1f27;
    --page: #f4f5f5;
    --white: #ffffff;
    --band: #eceeee;
    --text: #3a3d3f;
    --muted: #6f7476;
    --line: #e9ebeb;
  }
  * { margin: 0; padding: 0; box-sizing: border-box; }
  html, body { width: 1200px; height: 3258px; overflow: hidden; }
  body {
    position: relative;
    background: var(--page);
    font-family: "Arimo", Arial, sans-serif;
    color: var(--text);
  }
  a { color: inherit; }

  .preheader {
    position: absolute; top: 30px; left: 149px; width: 902px;
    display: flex; justify-content: space-between; align-items: center;
    font-size: 22px;
  }
  .preheader-links a { margin-right: 30px; color: var(--text); }
  .preheader-call { color: var(--red); }
  .preheader-call strong { font-weight: 700; }

  .sheet {
    position: absolute; top: 90px; left: 149px; width: 902px; height: 2807px;
    background: var(--white);
    border-top: 13px solid var(--red);
  }

  .brand {
    position: absolute; top: 200px; left: 0; width: 100%;
    display: flex; justify-content: center; align-items: center; gap: 22px;
  }
  .brand-dot { width: 34px; height: 34px; border-radius: 50%; background: var(--red); }
  .brand-name { font-size: 62px; font-weight: 700; color: var(--red); letter-spacing: -1px; }

  .hero-visual {
    position: absolute; top: 312px; left: 299px; width: 312px; height: 380px;
    background: linear-gradient(180deg, #6e7275 0%, #2a2b2d 45%, #111213 100%);
    border-radius: 6px 6px 18px 18px;
  }
  .hero-title {
    position: absolute; top: 808px; left: 90px; width: 722px;
    text-align: center; color: var(--red); font-size: 40px; line-height: 50px; font-weight: 400;
  }
  .hero-copy {
    position: absolute; top: 922px; left: 140px; width: 622px;
    text-align: center; font-size: 26px; line-height: 38px; color: var(--text);
  }
  .btn {
    display: flex; justify-content: center; align-items: center;
    background: var(--red); color: var(--white);
    font-weight: 700; text-decoration: none;
  }
  .hero-btn {
    position: absolute; top: 1059px; left: 304px; width: 272px; height: 60px; font-size: 28px;
  }
  .divider { position: absolute; top: 1170px; left: 0; width: 902px; height: 60px; }

  .card {
    position: absolute; width: 426px; height: 345px;
    border: 2px solid var(--line); background: var(--white);
  }
  .card-title {
    position: absolute; top: 12px; left: 0; width: 100%;
    text-align: center; font-size: 26px; color: var(--text);
  }
  .card-visual { position: absolute; }
  .card-btn {
    position: absolute; left: -2px; bottom: -2px; width: 426px; height: 46px; font-size: 26px;
  }
  .col-a { left: 17px; }
  .col-b { left: 459px; }
  .row-1 { top: 1325px; }
  .row-2 { top: 1730px; }
  .row-3 { top: 2134px; }

  .more-band {
    position: absolute; left: 0; top: 2585px; width: 902px; height: 209px; background: var(--band);
  }
  .more-btn {
    position: absolute; top: 73px; left: 272px; width: 361px; height: 60px; font-size: 28px;
  }

  .footer { position: absolute; top: 2918px; left: 149px; width: 902px; font-size: 21px; color: var(--muted); }
  .footer-optout { margin-bottom: 28px; }
  .footer-optout a { color: var(--muted); }
  .footer-company { color: var(--red); font-weight: 700; line-height: 32px; }
  .footer-lines { line-height: 32px; margin-bottom: 14px; }
</style>
</head>
<body>
  <div class="preheader">
    <div class="preheader-links">
      <a href="#">View this newsletter online</a>
      <a href="#">Unsubscribe</a>
    </div>
    <div class="preheader-call">Call us now on <strong>1300 555 018</strong></div>
  </div>

  <main class="sheet">
    <div class="brand">
      <span class="brand-dot"></span>
      <span class="brand-name">Loft Merchandise</span>
    </div>

    <div class="hero-visual" role="img" aria-label="Black tote bag with grey and white striped panel"></div>
    <h1 class="hero-title">Fusce urna arcu, pharetra vel metus ut efficitur vehicula metus</h1>
    <p class="hero-copy">Lorem Ipsum is simply dummy text of the printing and typesetting industry. Lorem Ipsum has been the industry's standard dummy text ever since the 1500s</p>
    <a class="btn hero-btn" href="#">Request Sample</a>

    <svg class="divider" viewBox="0 0 902 60" aria-hidden="true">
      <polyline points="0,10 451,40 902,10" fill="none" stroke="#eef0f0" stroke-width="3"/>
    </svg>

    <section class="card col-a row-1">
      <p class="card-title">Lorem ipsum dolor sit amet</p>
      <div class="card-visual" role="img" aria-label="Black cooler backpack" style="top:80px;left:148px;width:126px;height:180px;background:linear-gradient(180deg,#3a3b3d,#0f1011);border-radius:14px;"></div>
      <a class="btn card-btn" href="#">Request Sample</a>
    </section>
    <section class="card col-b row-1">
      <p class="card-title">Lorem ipsum dolor sit amet</p>
      <div class="card-visual" role="img" aria-label="Row of coloured oval keyrings" style="top:150px;left:118px;width:190px;height:44px;background:linear-gradient(90deg,#e08a20,#c92a20,#2a3a70,#2e8a40,#222);border-radius:22px;"></div>
      <a class="btn card-btn" href="#">Request Sample</a>
    </section>

    <section class="card col-a row-2">
      <p class="card-title">Lorem ipsum dolor sit amet</p>
      <div class="card-visual" role="img" aria-label="Group of coloured drawstring bags" style="top:80px;left:118px;width:190px;height:172px;background:linear-gradient(135deg,#2a2b2d,#d8502a 40%,#3360b0 70%,#2a2b2d);border-radius:8px;"></div>
      <a class="btn card-btn" href="#">Request Sample</a>
    </section>
    <section class="card col-b row-2">
      <p class="card-title">Lorem ipsum dolor sit amet</p>
      <div class="card-visual" role="img" aria-label="Stack of printed lunch bags in bright colours" style="top:78px;left:150px;width:126px;height:176px;background:linear-gradient(180deg,#3a8ad0,#f2c020 35%,#e8a020 60%,#e04080 85%,#2a2b2d);border-radius:8px;"></div>
      <a class="btn card-btn" href="#">Request Sample</a>
    </section>

    <section class="card col-a row-3">
      <p class="card-title">Lorem ipsum dolor sit amet</p>
      <div class="card-visual" role="img" aria-label="Rainbow range of non-woven tote bags" style="top:80px;left:118px;width:190px;height:178px;background:linear-gradient(90deg,#f0e040,#f080b0 30%,#e03030 50%,#40a040 70%,#2040a0);border-radius:6px;"></div>
      <a class="btn card-btn" href="#">Request Sample</a>
    </section>
    <section class="card col-b row-3">
      <p class="card-title">Lorem ipsum dolor sit amet</p>
      <div class="card-visual" role="img" aria-label="Fan of coloured satchels" style="top:120px;left:118px;width:190px;height:104px;background:linear-gradient(90deg,#e8e8e8,#f0a020 30%,#e03020 50%,#30a040 70%,#2a50b0 85%,#222);border-radius:6px;"></div>
      <a class="btn card-btn" href="#">Request Sample</a>
    </section>

    <div class="more-band">
      <a class="btn more-btn" href="#">Browse Other Products</a>
    </div>
  </main>

  <footer class="footer">
    <p class="footer-optout">Don't want these emails anymore? <a href="#">Unsubscribe here.</a></p>
    <p class="footer-company">Loft Merchandise</p>
    <p class="footer-lines">
      Unit 4, 12 Station Rd, Ashwood, Vic 3147<br>
      Tel : 1300 555 018<br>
      Fax : 1300 555 019<br>
      Email: info@loftmerchandise.example.au
    </p>
    <p>Copyright © 2014 Loft Merchandise</p>
  </footer>
</body>
</html>
```